a residential painting contractor I need a 6x9 postcard made

I already have a logo, I'm trying to offer my services to people. you can put that there's a 250$ discount for first time customers. include my License number #4627381 as well as the services I offer, interior and exterior painting, pressure washing, cabinet painting, epoxy floors, wood staining, decks, fences and much more. I'm licensed bonded and insured as well.

Target Market(s)

residential consumers (homeowners)

Industry/Entity Type

Painting contractor

Requirements
Must have
• postage stuff on the back I've linked some pictures top right please, my license number, what I do, phone number (555)317-0846 email velbrushworks7@mailzo.net, front and back of postcard
Nice to have
• well lit house in the background, maybe little circles of people doing some of the services I offer

```html
<!DOCTYPE html>
<html lang="en">
<head>
<meta charset="utf-8">
<title>Vel Brushworks – Residential Painting Postcard</title>
<link href="https://fonts.googleapis.com/css2?family=Outfit:wght@300;400;600;700;800&display=swap" rel="stylesheet">
<style>
  :root {
    --royal: #22408a;
    --orange: #f7941d;
    --sky: #aecbeb;
    --footer: #2e2f6c;
    --white: #ffffff;
    --navy: #1d2f6b;
  }
  * { box-sizing: border-box; margin: 0; padding: 0; }
  html, body { width: 1200px; height: 1004px; overflow: hidden; background: #fff; }
  body { position: relative; font-family: "Outfit", sans-serif; }

  .postcard {
    position: absolute; left: 221px; top: 249px; width: 758px; height: 506px;
    background: var(--royal); overflow: hidden; color: var(--white);
  }
  .sky-beam { position: absolute; inset: 0; }
  .trust-tab {
    position: absolute; left: 0; top: 0; width: 385px; height: 32px;
    background: var(--orange); border-bottom-right-radius: 18px;
    font-size: 11px; font-weight: 700; letter-spacing: 4px;
    padding-left: 55px; line-height: 33px;
  }
  .headline { position: absolute; left: 54px; top: 44px; font-weight: 700; line-height: 1; }
  .headline .line-1 { display: block; font-size: 49px; letter-spacing: -0.5px; }
  .headline .line-2 { display: block; font-size: 52px; margin-top: 4px; letter-spacing: -0.5px; }

  .services {
    position: absolute; left: 53px; top: 184px; width: 444px; height: 146px;
    border: 3px solid var(--orange); border-radius: 20px;
  }
  .services-tab {
    position: absolute; left: 175px; top: 167px; width: 199px; height: 39px;
    background: var(--orange); border-radius: 20px; color: var(--navy);
    font-size: 27px; font-weight: 700; text-align: center; line-height: 40px; letter-spacing: -0.5px;
  }
  .service {
    position: absolute; font-size: 21px; font-weight: 300; line-height: 1;
    display: flex; align-items: center; gap: 5px; white-space: nowrap;
  }
  .service svg { width: 15px; height: 15px; flex: none; }
  .service.cont { padding-left: 20px; }

  .offer-amount {
    position: absolute; left: 51px; top: 330px; font-size: 98px; font-weight: 700;
    color: var(--orange); letter-spacing: -4px; line-height: 1;
  }
  .offer-text { position: absolute; left: 268px; top: 347px; font-weight: 800; line-height: 1; }
  .offer-text .big { display: block; font-size: 35px; letter-spacing: -0.5px; }
  .offer-text .small { display: block; font-size: 22px; margin-top: 2px; letter-spacing: -0.3px; }

  .brand {
    position: absolute; left: 567px; top: 60px; width: 159px; text-align: center;
    font-weight: 700; color: var(--navy); font-size: 22px; line-height: 1.05;
  }
  .brand .dot { width: 78px; height: 78px; border-radius: 50%; background: var(--navy); margin: 0 auto 10px; }

  .house-art {
    position: absolute; left: 472px; top: 217px; width: 282px; height: 232px;
    background: linear-gradient(160deg, #e2c37f 0%, #d9534a 45%, #e8d4a6 75%, #7cb342 100%);
    border-radius: 18px; opacity: 0.9;
  }
  .license { position: absolute; right: 8px; top: 409px; text-align: right; font-weight: 700; line-height: 1.25; }
  .license .label { display: block; font-size: 7px; letter-spacing: 1.5px; }
  .license .number { display: block; font-size: 12px; letter-spacing: 2.5px; }

  .contact-bar {
    position: absolute; left: 0; bottom: 0; width: 758px; height: 70px;
    background: var(--footer); display: flex; align-items: center; justify-content: center;
    gap: 14px; font-size: 31px; font-weight: 600; letter-spacing: -0.5px;
  }
  .contact-bar svg { flex: none; }
  .contact-bar .divider { font-weight: 300; }
</style>
</head>
<body>
  <section class="postcard">
    <svg class="sky-beam" width="758" height="506" viewBox="0 0 758 506" aria-hidden="true">
      <polygon points="559,0 758,0 758,114 719,436 506,436" fill="var(--sky)"/>
    </svg>

    <div class="trust-tab">LICENSED, BONDED AND INSURED</div>

    <h1 class="headline">
      <span class="line-1">Residential Painting</span>
      <span class="line-2">CONTRACTOR</span>
    </h1>

    <div class="services"></div>
    <div class="services-tab">SERVICES</div>

    <svg width="0" height="0" style="position:absolute" aria-hidden="true">
      <symbol id="tick" viewBox="0 0 16 16">
        <circle cx="8" cy="8" r="6.8" fill="none" stroke="#f7941d" stroke-width="1.6"/>
        <path d="M4.8 8.2l2.2 2.2 4.2-4.6" fill="none" stroke="#f7941d" stroke-width="1.6" stroke-linecap="round" stroke-linejoin="round"/>
      </symbol>
    </svg>

    <div class="service" style="left:70px; top:213px"><svg><use href="#tick"/></svg>Interior And</div>
    <div class="service cont" style="left:70px; top:238px">Exterior Painting</div>
    <div class="service" style="left:70px; top:264px"><svg><use href="#tick"/></svg>Pressure Washing</div>
    <div class="service" style="left:70px; top:289px"><svg><use href="#tick"/></svg>Cabinet Painting</div>

    <div class="service" style="left:290px; top:213px"><svg><use href="#tick"/></svg>Epoxy Floors</div>
    <div class="service" style="left:290px; top:238px"><svg><use href="#tick"/></svg>Wood Staining</div>
    <div class="service" style="left:290px; top:264px"><svg><use href="#tick"/></svg>Decks <svg style="margin-left:3px"><use href="#tick"/></svg>Fences</div>
    <div class="service cont" style="left:290px; top:289px">And Much More</div>

    <div class="offer-amount">250$</div>
    <div class="offer-text">
      <span class="big">DISCOUNT</span>
      <span class="small">FOR FIRST TIME</span>
      <span class="small">CUSTOMERS</span>
    </div>

    <div class="brand"><div class="dot"></div>VEL BRUSHWORKS</div>

    <div class="house-art" role="img" aria-label="Illustration of a house under renovation with painters working inside and outside"></div>

    <div class="license">
      <span class="label">LICENSE NUMBER</span>
      <span class="number">#4627381</span>
    </div>

    <footer class="contact-bar">
      <svg width="30" height="30" viewBox="0 0 24 24" aria-hidden="true">
        <path fill="#f7941d" d="M6.6 10.8a15.1 15.1 0 0 0 6.6 6.6l2.2-2.2c.3-.3.7-.4 1-.2 1.1.4 2.3.6 3.6.6.6 0 1 .4 1 1V20c0 .6-.4 1-1 1A17 17 0 0 1 3 4c0-.6.4-1 1-1h3.5c.6 0 1 .4 1 1 0 1.3.2 2.5.6 3.6.1.3 0 .7-.2 1z"/>
      </svg>
      <span>(555) 317-0846</span>
      <span class="divider">|</span>
      <svg width="32" height="26" viewBox="0 0 32 24" aria-hidden="true">
        <rect x="1" y="2" width="30" height="20" rx="2" fill="#f7941d"/>
        <path d="M2 4l14 10L30 4" fill="none" stroke="var(--footer)" stroke-width="2.2"/>
      </svg>
      <span>velbrushworks7@mailzo.net</span>
    </footer>
  </section>
</body>
</html>
```